Autodetailing namecard design: Rose Gold Lettering on Black Matt

This is a namecard design project
requiring two-sided design
Base Color of Namecard: black matt

On front:
Company name,
"Lumen Finishes 47 Kelapa"
Subtext: Auto Detailing Studio

Name of card holder: Dennis Lowe
Phone Number: +6012-4837-5062
address: 47, Jalan Kelapa 3/5Taman Seri Kelapa, 81200 Johor Bahru, Johor, Malaysia

Back:
Our Services
High Gloss Car Paint Protection
Custom Color Modification and Styling
Anti-Chip Glass Protection Film
Heat Rejection Glass Tinting

Target Market(s)

Autodetailing for highend cars

Contact Information for Business Card

as mentioned in project details

Colors

Designer to choose colors to be used in the design.

Requirements
Must have
• The main value-add to this project is the design of a logo suited for our purpose and name, and the inclusion of business card details into the card design

```html
<!DOCTYPE html>
<html lang="en">
<head>
<meta charset="UTF-8">
<title>Lumen Finishes 47 Kelapa – Business Card</title>
<link rel="stylesheet" href="https://fonts.googleapis.com/css2?family=Josefin+Sans:wght@400;600&family=Open+Sans:wght@400;600;700&display=swap">
<style>
  :root {
    --page-bg: #e4e4e6;
    --card-matte: #151515;
    --rose-gold: #d9a38f;
    --rose-gold-soft: #c99684;
    --body-light: #e8d6cf;
    --panel-tint: rgba(217,163,143,0.10);
    --card-shadow: 0 14px 30px rgba(0,0,0,0.32);
  }
  * { box-sizing: border-box; margin: 0; padding: 0; }
  html, body { width: 1200px; height: 1200px; overflow: hidden; }
  body { background: var(--page-bg); position: relative; font-family: "Open Sans", sans-serif; }

  .card {
    position: absolute;
    width: 580px;
    height: 332px;
    border-radius: 30px;
    box-shadow: var(--card-shadow);
    overflow: hidden;
    background: var(--card-matte);
    color: var(--body-light);
  }
  .card--back { left: 70px; top: 150px; }
  .card--front { left: 550px; top: 640px; }

  .wordmark {
    position: absolute;
    text-align: center;
    font-family: "Josefin Sans", sans-serif;
    font-weight: 600;
    text-transform: uppercase;
    line-height: 1;
    color: var(--rose-gold);
  }
  .wordmark__line { display: block; font-size: 30px; letter-spacing: 2px; }
  .wordmark__line + .wordmark__line { margin-top: 4px; }
  .tagline {
    display: block;
    font-family: "Josefin Sans", sans-serif;
    font-weight: 400;
    font-size: 14px;
    letter-spacing: 8px;
    margin-top: 10px;
    text-transform: uppercase;
    color: var(--rose-gold-soft);
  }

  .card--back .wordmark { left: 0; right: 0; top: 60px; }

  .services { position: absolute; left: 0; right: 0; top: 200px; text-align: center; }
  .services__title {
    display: inline-block;
    font-size: 13px; font-weight: 600; text-decoration: underline;
    text-underline-offset: 3px; letter-spacing: 0.3px;
    color: var(--rose-gold);
  }
  .services__list {
    margin: 14px auto 0;
    width: 470px;
    padding: 8px 10px;
    background: var(--panel-tint);
    border-radius: 4px;
    font-size: 11.5px; line-height: 1.45;
  }

  .card--front .wordmark { left: 70px; width: 480px; top: 52px; }

  .holder { position: absolute; left: 46px; top: 192px; }
  .holder__name { font-size: 22px; font-weight: 700; color: var(--rose-gold); letter-spacing: -0.3px; line-height: 1.1; }
  .holder__role { font-size: 11px; letter-spacing: 0.6px; text-transform: uppercase; }
  .rule { display: block; width: 26px; height: 2px; background: var(--rose-gold); margin: 8px 0 7px; }
  .contact-list { list-style: none; font-size: 12px; line-height: 1.55; }
  .contact-list li { display: flex; align-items: center; gap: 7px; }
  .contact-list svg { width: 11px; height: 11px; fill: var(--rose-gold); flex: none; }

  .address { position: absolute; left: 350px; top: 192px; font-size: 12px; line-height: 1.5; }
</style>
</head>
<body>

<section class="card card--back" aria-label="Card back">
  <div class="wordmark">
    <span class="wordmark__line">Lumen</span>
    <span class="wordmark__line">Finishes 47 Kelapa</span>
    <span class="tagline">Auto Detailing Studio</span>
  </div>
  <div class="services">
    <span class="services__title">OUR SERVICES:</span>
    <p class="services__list">
      High Gloss Car Paint Protection. Custom Color Modification and Styling<br>
      Anti-Chip Glass Protection Film. Heat Rejection Glass Tinting
    </p>
  </div>
</section>

<section class="card card--front" aria-label="Card front">
  <div class="wordmark">
    <span class="wordmark__line">Lumen</span>
    <span class="wordmark__line">Finishes 47 Kelapa</span>
    <span class="tagline">Auto Detailing Studio</span>
  </div>

  <div class="holder">
    <p class="holder__name">Dennis Lowe</p>
    <p class="holder__role">Manager</p>
    <span class="rule"></span>
    <ul class="contact-list">
      <li>
        <svg viewBox="0 0 24 24" aria-hidden="true"><path d="M6.6 10.8a15.1 15.1 0 0 0 6.6 6.6l2.2-2.2c.3-.3.7-.4 1-.2 1.1.4 2.3.6 3.6.6.6 0 1 .4 1 1V20c0 .6-.4 1-1 1A17 17 0 0 1 3 4c0-.6.4-1 1-1h3.5c.6 0 1 .4 1 1 0 1.3.2 2.5.6 3.6.1.3 0 .7-.2 1z"/></svg>
        +6012-4837-5062
      </li>
      <li>
        <svg viewBox="0 0 24 24" aria-hidden="true"><path d="M2 5h20v14H2z M2 5l10 8 10-8"/></svg>
        studio@lumenfinishes.my
      </li>
      <li>
        <svg viewBox="0 0 24 24" aria-hidden="true"><circle cx="12" cy="12" r="10"/></svg>
        www.lumenfinishes.my
      </li>
    </ul>
  </div>

  <div class="address">
    <span class="rule"></span>
    <p>47, Jalan Kelapa 3/5<br>Taman Seri Kelapa, 81200<br>Johor Bahru, Johor, Malaysia</p>
  </div>
</section>

</body>
</html>
```